Auto Detailing Facility Needs Facebook Cover Photo

Looking for a beautiful Facebook cover photo using our logo and a photo, including our business information. Does not have to use the photo provided but the logo must be in there. I want an eye-catching cover photo that promotes the luxury brand.

Website: www.glossbayauto.com
Phone: 508-555-0147
Address: 412 Lower Maple Rd Unit B-3 Franklin, MA 02091

Industry/Entity Type

Automotive

Colors

Designer to choose colors to be used in the design.

```html
<!DOCTYPE html>
<html lang="en">
<head>
<meta charset="utf-8">
<title>Gloss Bay Auto – Facebook Cover Concepts</title>
<link rel="stylesheet" href="https://fonts.googleapis.com/css2?family=Montserrat:wght@400;500&display=swap">
<style>
  :root {
    --sheet-top: #e6e6e6;
    --sheet-mid: #fbfbfb;
    --ink: #1c1c1c;
    --banner-dark: #050505;
    --banner-smoke: #151a1f;
    --brand-white: #ffffff;
    --brand-green: #5cb548;
    --button-green: #3f7f3c;
    --accent-yellow: #e7b21c;
    --footer-grey: #c9c9c9;
    --rule-green: #2f6b2c;
  }
  * { box-sizing: border-box; margin: 0; padding: 0; }
  html, body { width: 904px; height: 1200px; overflow: hidden; }
  body {
    position: relative;
    font-family: "Montserrat", "Helvetica Neue", Arial, sans-serif;
    background: radial-gradient(ellipse at 50% 45%, var(--sheet-mid) 0%, var(--sheet-top) 100%);
    color: var(--ink);
  }
  .sheet-title {
    position: absolute; top: 28px; left: 0; width: 904px;
    text-align: center; font-size: 18px; font-weight: 400;
  }
  .sample-label {
    position: absolute; left: 55px; font-size: 17px; font-weight: 400;
  }
  .cover {
    position: absolute; left: 55px; width: 794px; height: 302px;
    overflow: hidden;
    background: radial-gradient(ellipse at 20% 30%, var(--banner-smoke) 0%, var(--banner-dark) 60%);
    box-shadow: 0 2px 6px rgba(0,0,0,.35);
  }
  .cover--one { top: 81px; }
  .cover--two { top: 449px; }
  .cover--three { top: 814px; }

  .brand-name {
    position: absolute; color: var(--brand-white);
    font-weight: 400; letter-spacing: .06em; white-space: nowrap;
  }
  .tagline {
    position: absolute; color: var(--brand-green);
    font-weight: 400; white-space: nowrap; text-transform: uppercase;
  }
  .footer-line {
    position: absolute; left: 0; width: 794px; top: 262px;
    text-align: center; font-size: 15.5px; color: var(--footer-grey);
    letter-spacing: -.02em; white-space: nowrap;
  }
  .footer-line .sep { margin: 0 14px; }
  .book-button {
    position: absolute; left: 262px; top: 206px; width: 272px; height: 37px;
    border-radius: 19px; background: var(--button-green);
    color: var(--brand-white); font-size: 16px; line-height: 37px;
    text-align: center; letter-spacing: -.01em;
  }

  /* Cover one */
  .cover--one .car-photo {
    position: absolute; left: 384px; top: 30px; width: 410px; height: 214px;
    border-radius: 60px 0 0 30px;
    background: linear-gradient(160deg, #f5c826 0%, #e3a90f 55%, #2a2a2a 100%);
  }
  .cover--one .brand-name { left: 30px; top: 72px; font-size: 24px; }
  .cover--one .tagline { left: 24px; top: 116px; font-size: 22px; line-height: 27px; }
  .cover--one .divider {
    position: absolute; left: 24px; width: 186px; height: 1px;
    background: linear-gradient(90deg, var(--rule-green), transparent);
  }
  .cover--one .divider--upper { top: 182px; }
  .cover--one .divider--lower { top: 252px; }
  .cover--one .book-prompt {
    position: absolute; left: 24px; top: 194px;
    font-size: 15px; color: var(--brand-green);
  }
  .cover--one .call-line {
    position: absolute; left: 24px; top: 212px;
    font-size: 27px; color: var(--brand-white); letter-spacing: -.01em;
  }
  .cover--one .contact-line {
    position: absolute; left: 23px; top: 267px;
    font-size: 14.5px; color: var(--accent-yellow); letter-spacing: -.02em; white-space: nowrap;
  }
  .cover--one .contact-line .sep { margin: 0 12px; }

  /* Cover two */
  .cover--two .brand-name {
    left: 0; width: 794px; top: 88px; text-align: center; font-size: 44px;
  }
  .cover--two .tagline {
    left: 0; width: 794px; top: 155px; text-align: center; font-size: 25px;
  }

  /* Cover three */
  .cover--three .truck-photo {
    position: absolute; inset: 0;
    background: linear-gradient(100deg, #1a1c1f 0%, #0d0e10 45%, #16171a 100%);
  }
  .cover--three .brand-name {
    left: 0; width: 794px; top: 126px; text-align: center; font-size: 50px;
  }
</style>
</head>
<body>
  <h1 class="sheet-title">Auto Detailing Facility Needs Facebook Cover Photo</h1>

  <section class="cover cover--one">
    <div class="car-photo" role="img" aria-label="Yellow sports car, front three-quarter view"></div>
    <div class="brand-name">GLOSS BAY AUTO</div>
    <p class="tagline">Bringing detailing<br>to your doorstep</p>
    <div class="divider divider--upper"></div>
    <p class="book-prompt">READY TO BOOK?</p>
    <p class="call-line">CALL 508-555-0147</p>
    <div class="divider divider--lower"></div>
    <p class="contact-line">www.glossbayauto.com<span class="sep">|</span>412 Lower Maple Rd Unit B-3 Franklin, MA 02091</p>
  </section>
  <p class="sample-label" style="top:398px">Sample&nbsp; 1</p>

  <section class="cover cover--two">
    <div class="brand-name">GLOSS BAY AUTO</div>
    <p class="tagline">Bringing detailing to your doorstep</p>
    <div class="book-button">BOOK YOUR APPOINTMENT</div>
    <p class="footer-line">508-555-0147<span class="sep">|</span>www.glossbayauto.com<span class="sep">|</span>412 Lower Maple Rd Unit B-3 Franklin, MA 02091</p>
  </section>
  <p class="sample-label" style="top:761px">Sample&nbsp; 2</p>

  <section class="cover cover--three">
    <div class="truck-photo" role="img" aria-label="Darkened photo of service vans and a pickup truck"></div>
    <div class="brand-name">GLOSS BAY AUTO</div>
    <div class="book-button">BOOK YOUR APPOINTMENT</div>
    <p class="footer-line">508-555-0147<span class="sep">|</span>www.glossbayauto.com<span class="sep">|</span>412 Lower Maple Rd Unit B-3 Franklin, MA 02091</p>
  </section>
  <p class="sample-label" style="top:1131px">Sample&nbsp; 3</p>
</body>
</html>
```